Beauty Salon Industry - Web Design Project

zQuarta is a well-funded start up developing an Online Marketing Platform for small businesses in Europe.
We require a large number of high quality business web designs for our business website builder. Our business websites are seamlessly integrated into our Online Marketing systems and therefore it is important for designers to comply with our Design Guidelines.
This is our second contest and it will focus on the beauty salon industry. We will be running contents every 2-3 weeks for a new industry. Last month, we ran a contest for Builder website designs with 3 top prizes (plus £10 per variation) and we also paid out £25 per design for 20+ entries from designers who did not win the top prizes. So we encourage all entries!
We have included a wire frame this time to encourage you to be as creative as possible with your designs and layout while respecting the following guidelines:
1) You CAN change the layout as much as you like. If you think a vertical menu would look better, then use it. If you think the design would benefit from moving an element to a different location, then you can do that too.
2) You must include ALL the elements in the wire frame in your design.(e.g. latest 2 news entries, a testimonial, 1 gallery image, carousel etc...). Please make sure you have looked through the wire frame and know what is required. Entries that do not include all the elements will not qualify to win.
3) So remember, you CAN change the layout as much as you like but DO NOT remove any elements nor move them to a different page.
4) You may change the size and style of the carousel image. We would like to see as many variations of this as possible.
We are rewarding 3 prizes, and would like the winning designer to design the internal pages to the new design.
As always, if we think your designs could be incorporated into our system, but you do not win the competition, we will reward £25. Therefore, we encourage designers to submit as many designs as possible as we may award up to 25 designs.
Judging criteria : -
1) Visual Design
2) Layout must adhere to best practices and wireframe. If you decide to move elements around significantly please provide reason
3) Functional, informative and drives calls to action
Updates
As usual:
1st place = £350
2nd place = £250
3rd place = £150
Good luck!
Very happy with all the designs submitted so far, and will provide feedback ASAP.
We would like to see you try arranging the elements differently. So please try different navigation types and layouts.
Thanks
Morris
Prize funds for 1st place has been slightly increased.
Thanks
Morris
We have already had some amazing designs submitted. Thanks.
Remember to play with the layout of the elements and try designs with a carousel/slider that is in portrait not just in landscape.
Thanks everyone!
Morris
Hi everyone, we are really enjoying looking through the designs.
We have one NEW requirement. If you have used an image from http://www.frelik-example.com/ in your design, could you please replace it with another.
We are not associated with them.
Thank you.
I have just sent a poll around the office to vote on all the designs and hope to have the results soon.
Good luck and I hope to see all your great designs for our next project in a couple of weeks.
Morris
Hi everyone, we hope you have had a good holiday season. We will be rewarding the prizes very soon, hopefully today or tomorrow.
Thanks
Morris
We are currently going through all the designs that did not win our competition and will be contacting the designers of the designs we would like to use in our system, so please keep an eye on your inbox over the next few days.
Thank you
Morris
Target Market(s)
Beauty Salon Industry
Industry/Entity Type
Beauty Salon
Look and feel
Each slider illustrates characteristics of the customer's brand and the style your logo design should communicate.

```html
<!DOCTYPE html>
<html lang="en">
<head>
<meta charset="utf-8">
<title>Velvet Air – Hair and Urban Spa</title>
<link rel="stylesheet" href="https://fonts.googleapis.com/css2?family=Cinzel:wght@400;700&family=Arimo:ital,wght@0,400;0,700;1,400;1,700&display=swap">
<style>
:root{
  --bg:#eeecf1;
  --purple:#8e3a9d;
  --purple-dark:#6d2479;
  --purple-soft:#b27bbd;
  --green:#6cb52a;
  --green-dark:#4f9a17;
  --nav-top:#5a5a5a;
  --nav-bottom:#2b2b2b;
  --text:#6a6a6a;
  --text-light:#9a9a9a;
  --white:#ffffff;
  --panel:#e2dfe7;
}
*{margin:0;padding:0;box-sizing:border-box}
html,body{width:1200px;height:1130px;overflow:hidden}
body{background:var(--bg);font-family:'Arimo',Arial,sans-serif;color:var(--text);position:relative}
.abs{position:absolute}

.brand{left:141px;top:38px}
.brand-name{font-family:'Cinzel',Georgia,serif;font-size:50px;color:var(--purple);line-height:1;letter-spacing:1px}
.brand-tag{font-family:'Cinzel',Georgia,serif;font-size:17px;color:#555;letter-spacing:1px;margin-top:6px}

.phone{right:115px;top:28px;font-family:'Cinzel',Georgia,serif;font-size:30px;color:var(--purple)}
.book-now{right:115px;top:70px;width:165px;height:36px;background:linear-gradient(var(--purple),var(--purple-dark));color:var(--white);font-family:'Cinzel',Georgia,serif;font-size:18px;display:flex;align-items:center;justify-content:center;border-radius:2px}

.main-nav{left:0;top:141px;width:1200px;height:56px;background:linear-gradient(var(--nav-top),var(--nav-bottom));box-shadow:0 6px 10px rgba(0,0,0,.12)}
.nav-item{position:absolute;top:12px;color:var(--white)}
.nav-item b{display:block;font-size:14px;font-weight:700}
.nav-item span{display:block;font-size:11px;color:#aaa;margin-top:3px}

.intro{left:115px;top:228px;width:195px}
.intro h1{font-family:'Cinzel',Georgia,serif;font-weight:400;font-size:20px;line-height:27px;color:var(--purple)}
.intro p{font-size:13.5px;line-height:20px;margin-top:14px}
.intro em{color:var(--purple);font-weight:700}
.intro strong{color:var(--purple)}
.more-link{left:115px;top:562px;font-family:'Cinzel',Georgia,serif;font-size:14px;color:#666}
.bullet{display:inline-block;width:8px;height:8px;margin-right:8px;background:radial-gradient(circle,var(--purple) 1.5px,transparent 2px) 0 0/4px 4px}

.gallery-thumb{left:115px;top:610px;width:190px;height:144px;background:linear-gradient(135deg,#c9c7cc,#6a6a70 60%,#3c3c40)}
.gallery-link{left:115px;top:764px;font-family:'Cinzel',Georgia,serif;font-size:14px;color:#666}

.carousel{left:331px;top:228px;width:530px;height:334px;background:radial-gradient(ellipse at 55% 45%,#f0d8c0,#c9a27a 45%,#e7e3e8 75%);box-shadow:0 6px 10px rgba(0,0,0,.15)}
.car-arrow{top:148px;width:32px;height:32px;background:var(--white);display:flex;align-items:center;justify-content:center}
.car-dots{right:22px;bottom:12px;display:flex;gap:6px}
.car-dots i{width:9px;height:9px;border-radius:50%;background:#d8d8d8;display:block}
.car-dots i.on{background:#555}

.testimonial{left:336px;top:576px;width:545px}
.testimonial q{display:block;font-family:'Cinzel',Georgia,serif;font-size:16.5px;line-height:26px;color:#555;quotes:"\201C" "";white-space:nowrap}
.testimonial cite{display:block;font-family:'Cinzel',Georgia,serif;font-style:normal;font-size:13px;color:#888;margin-top:6px}

.news-bar{left:333px;top:666px;width:528px;height:18px;border-bottom:1px solid #d7d3dc}
.news-label{left:205px;top:0;background:#d9d5df;padding:3px 12px;font-family:'Cinzel',Georgia,serif;font-size:11px;color:#555}
.news-all{right:6px;top:2px;font-size:11px;color:var(--text-light)}
.news{top:700px;width:250px}
.news h3{font-family:'Cinzel',Georgia,serif;font-weight:400;font-size:16px;color:var(--purple)}
.news p{font-size:11.5px;line-height:17px;color:#888;margin-top:8px}
.news time{display:block;font-size:12px;color:#555;margin-top:10px}

.gift-card{left:883px;top:230px;width:202px;height:224px;background:var(--panel);overflow:hidden}
.gift-card p{position:absolute;left:21px;top:118px;font-size:13.5px;line-height:19px;color:var(--purple)}
.gift-card p b{font-weight:700}
.gift-btn{left:20px;top:168px;width:164px;height:34px;background:linear-gradient(var(--purple),var(--purple-dark));color:var(--white);font-family:'Cinzel',Georgia,serif;font-size:13.5px;display:flex;align-items:center;justify-content:center}
.gift-price{right:14px;top:10px;color:var(--white);font-family:'Arimo',Arial,sans-serif;font-weight:700;font-size:32px}

.side-head{font-family:'Cinzel',Georgia,serif;font-size:17px;color:#666;display:flex;align-items:center;gap:10px}
.address{left:885px;top:484px}
.address p{font-size:11.5px;line-height:19px;color:var(--purple-soft);margin:8px 0 0 26px}
.map-link{left:1000px;top:566px;font-size:11.5px;color:var(--purple);font-weight:700;display:flex;align-items:center;gap:6px}
.map-link i{display:block;width:24px;height:22px;background:linear-gradient(#f3e08a,#e0b23c)}
.hours{left:885px;top:614px}
.hours ul{list-style:none;margin:10px 0 0 26px}
.hours li{font-size:11.5px;line-height:25px;color:var(--purple-soft)}

.partner{top:843px;width:230px;height:137px}
.partner span{position:absolute;left:0;bottom:0;background:rgba(255,255,255,.9);font-family:'Cinzel',Georgia,serif;font-size:13px;color:#555;padding:6px 12px}

.site-footer{left:115px;top:1000px;width:970px;height:50px;background:linear-gradient(var(--green),var(--green-dark));color:var(--white);font-size:11.5px}
.site-footer .copy{left:20px;top:18px;color:#cfe9b6}
.site-footer .credit{right:20px;top:18px}
</style>
</head>
<body>

<div class="abs brand">
  <div class="brand-name">Velvet Air</div>
  <div class="brand-tag">Hair and Urban Spa</div>
</div>

<div class="abs phone">020 7946 0123</div>
<div class="abs book-now">Book Now</div>

<nav class="abs main-nav">
  <div class="nav-item" style="left:141px"><b>HOME</b><span>Velvet Air</span></div>
  <div class="nav-item" style="left:245px"><b>SERVICES</b><span>Our services</span></div>
  <div class="nav-item" style="left:369px"><b>GALLERY</b><span>Our portfolio</span></div>
  <div class="nav-item" style="left:487px"><b>TESTIMONIALS</b><span>What people say</span></div>
  <div class="nav-item" style="left:645px"><b>NEWS</b><span>What's happening</span></div>
  <div class="nav-item" style="left:754px"><b>ABOUT US</b><span>What we do</span></div>
  <div class="nav-item" style="left:885px"><b>CONTACT US</b><span>Reach us</span></div>
</nav>

<section class="abs intro">
  <h1>Let our hair and beauty skills blow you away</h1>
  <p><em>Velvet Air</em> is a passionate, creative team, dedicated to delivering a second to none, <em>personal salon experience</em> that will 'blow' your mind.</p>
  <p>Where ultimate <strong>hairdressing</strong> comes hand-in-hand with style, glamour, fashion, innovation and skill to create an exquisite salon experience in the heart of London.</p>
</section>
<div class="abs more-link"><span class="bullet"></span>More&gt;</div>

<div class="abs gallery-thumb" role="img" aria-label="Photo of a stylist colouring a client's hair"></div>
<div class="abs gallery-link"><span class="bullet"></span>View Gallery &gt;</div>

<div class="abs carousel" role="img" aria-label="Carousel photo of a model being styled with make-up brushes and a hair dryer">
  <div class="abs car-arrow" style="left:0">
    <svg width="12" height="16" viewBox="0 0 12 16"><path d="M9 2 3 8l6 6" fill="none" stroke="#333" stroke-width="3"/></svg>
  </div>
  <div class="abs car-arrow" style="right:0">
    <svg width="12" height="16" viewBox="0 0 12 16"><path d="M3 2l6 6-6 6" fill="none" stroke="#333" stroke-width="3"/></svg>
  </div>
  <div class="abs car-dots"><i class="on"></i><i></i><i></i></div>
</div>

<blockquote class="abs testimonial">
  <q>My hairstylist, Maribel, was truly amazing. She<br>listened to exactly what I wanted, but also more...</q>
  <cite>– Ines Carrow</cite>
</blockquote>

<div class="abs news-bar">
  <div class="abs news-label">Latest News</div>
  <div class="abs news-all">View all</div>
</div>

<article class="abs news" style="left:333px">
  <h3>Book Now for Christmas</h3>
  <p>Our salon is usually very busy for the two weeks before Christmas, so please book early: call 020 7946 0123, or contact us.</p>
  <time>1 Dec. 2011</time>
</article>
<article class="abs news" style="left:609px">
  <h3>Want to be a hair model?</h3>
  <p>Our salon is usually very busy for the two weeks before Christmas, so please book early: call 020 7946 0123, or contact us.</p>
  <time>1 Dec. 2011</time>
</article>

<aside class="abs gift-card">
  <svg class="abs" style="left:0;top:0" width="202" height="224">
    <polygon points="85,0 202,0 202,82" fill="#8e3a9d"/>
    <g fill="#6cb52a">
      <rect x="22" y="64" width="34" height="8"/>
      <rect x="25" y="74" width="28" height="22"/>
    </g>
    <path d="M39 64c-6-10-16-10-14-3 2 4 8 3 14 3zM39 64c6-10 16-10 14-3-2 4-8 3-14 3z" fill="none" stroke="#6cb52a" stroke-width="3"/>
    <rect x="37" y="64" width="4" height="32" fill="#e2dfe7"/>
  </svg>
  <div class="abs gift-price">£25</div>
  <p>Complimentary gift for<br><b>first-time clients!</b></p>
  <div class="abs gift-btn">Book appointment</div>
</aside>

<section class="abs address">
  <div class="side-head">
    <svg width="14" height="18" viewBox="0 0 14 18"><path d="M7 0a7 7 0 0 0-7 7c0 5 7 11 7 11s7-6 7-11a7 7 0 0 0-7-7z" fill="#b27bbd"/><circle cx="7" cy="7" r="2.5" fill="#eeecf1"/></svg>
    Velvet Address:
  </div>
  <p>12 Elm Mews<br>London W1X 3QA</p>
</section>
<div class="abs map-link">View Map <i></i></div>

<section class="abs hours">
  <div class="side-head">
    <svg width="16" height="16" viewBox="0 0 16 16"><circle cx="8" cy="8" r="7" fill="none" stroke="#b27bbd" stroke-width="2"/><path d="M8 4v4h3" fill="none" stroke="#b27bbd" stroke-width="2"/></svg>
    Business Hours
  </div>
  <ul>
    <li>Mon. 9 a.m - 5 p.m.</li>
    <li>Tue. 9 a.m - 5 p.m.</li>
    <li>Wed. 9 a.m - 5 p.m.</li>
    <li>Thu. 9 a.m - 5 p.m.</li>
    <li>Fri. 9 a.m - 5 p.m.</li>
    <li>Sat. 9 a.m - 5 p.m.</li>
  </ul>
</section>

<div class="abs partner" style="left:115px;background:linear-gradient(120deg,#e8f1f8,#9cc6e4)" role="img" aria-label="Partner product photo with a model and skincare bottles"><span>Lumiere</span></div>
<div class="abs partner" style="left:362px;background:linear-gradient(120deg,#f2ede8,#c0622c)" role="img" aria-label="Partner photo of a model with long copper hair"><span>Vellora</span></div>
<div class="abs partner" style="left:609px;background:linear-gradient(120deg,#dfeaf3,#f1e2d3)" role="img" aria-label="Partner photo of a model with an elegant updo"><span>Bramble "n" Bee</span></div>
<div class="abs partner" style="left:855px;background:linear-gradient(120deg,#b88a62,#5a3c28)" role="img" aria-label="Partner photo of a model with glossy brown hair"><span>Schwanfeld</span></div>

<footer class="abs site-footer">
  <div class="abs copy">©2011 VelvetAir.com All rights reserved</div>
  <div class="abs credit">Managed by zQuarta.com &nbsp;|&nbsp; Admin</div>
</footer>

</body>
</html>
```